Event Flyer - LGBT Camping Event

I have attached a poster I made (SampleFlyer.pdf) that has all the elements I want. Just don't like the layout and how things look. You can use any colors that make the poster work. I would like to incorporate the Campfest logo into the flyer (uploaded). You are welcome to grab elements from the event website to incorporate into your design (www.campfestmeadowlark.org). I included a couple of pictures to possibly use too. Please include all 8 sponsors and the two hosts are the logos on the bottom of sample flyer - Prairie Alliance & Pinecrest Trail Council. The flyer size needs to be 12"Wide x 17" Tall. Here is a dropbox link to a possible image to use. https://lnk.example/7qTzKwd

Please use the wording;

DON’T MISS this LGBT camping event!

Plan the highlight of your summer TODAY.

It’s almost time for the Rocky Mountain Region’s largest LGBT pride camping event: Campfest Meadowlark!
Join us August 8th-12th for 5 days of fun in a friendly, safe, LGBT affirming environment for everyone, from everywhere!

More Info or Register Online www.sagebrightfest.org

Target Market(s)

LGBT Campers

Industry/Entity Type

Event

Colors

Designer to choose colors to be used in the design.

Requirements
Must have
• Must have text outlined in project description, Campfest logo, sponsor logos and host logos.

```html
<!DOCTYPE html>
<html lang="en">
<head>
<meta charset="utf-8">
<title>Campfest – LGBT Camping Event</title>
<link rel="stylesheet" href="https://fonts.googleapis.com/css2?family=Archivo:wght@300;400;700;900&display=swap">
<style>
  :root {
    --green: #3dc21e;
    --white: #ffffff;
    --ink: #111111;
    --band: rgba(60, 60, 55, 0.55);
    --tile-dark: #1d1d1d;
    --tile-light: #ffffff;
    --tile-grey: #8a8c8c;
    --navy: #1f3f8f;
    --blue: #3aa9d8;
    --forest: #2e5a2a;
    --sun: #f2b23a;
  }
  * { box-sizing: border-box; margin: 0; padding: 0; }
  html, body { width: 857px; height: 1200px; overflow: hidden; background: var(--white); }
  body { font-family: "Archivo", Arial, sans-serif; color: var(--ink); }

  .flyer { position: relative; width: 857px; height: 1200px; overflow: hidden; background: var(--white); }

  .hero-photo {
    position: absolute; left: 0; top: 0; width: 857px; height: 743px;
    background:
      radial-gradient(ellipse at 60% 10%, #c9d9e3 0%, rgba(201,217,227,0) 18%),
      radial-gradient(ellipse at 75% 55%, #7b9a3e 0%, rgba(123,154,62,0) 45%),
      radial-gradient(ellipse at 20% 70%, #8b7a4e 0%, rgba(139,122,78,0) 40%),
      linear-gradient(180deg, #2c3a22 0%, #3e5a2a 35%, #6a8a3a 65%, #5f6e35 100%);
  }

  .event-mark {
    position: absolute; right: 34px; top: 30px;
    display: flex; align-items: center; gap: 10px;
    color: var(--white); font-weight: 900; font-size: 30px; letter-spacing: 0.5px;
    text-shadow: 0 2px 6px rgba(0,0,0,0.35);
  }

  .headline {
    position: absolute; left: 78px; top: 128px;
    color: var(--white); text-transform: uppercase; line-height: 1.02;
    text-shadow: 0 2px 6px rgba(0,0,0,0.35);
  }
  .headline .strong { display: block; font-weight: 900; font-size: 56px; letter-spacing: -0.5px; }
  .headline .light { display: block; font-weight: 300; font-size: 65px; letter-spacing: -0.5px; }

  .sponsor-band {
    position: absolute; left: 0; top: 606px; width: 857px; height: 137px;
    background: var(--band);
  }
  .sponsor-label {
    position: absolute; left: 31px; top: 10px;
    color: var(--white); font-size: 23px; font-weight: 400;
  }
  .sponsor-tile {
    position: absolute; top: 48px; height: 77px;
    display: flex; align-items: center; justify-content: center; text-align: center;
    font-weight: 700; font-size: 15px; line-height: 1.1; padding: 0 6px;
  }
  .tile-grey { background: var(--tile-grey); color: var(--white); }
  .tile-light { background: var(--tile-light); color: var(--navy); }
  .tile-dark { background: var(--tile-dark); color: var(--white); }
  .sponsor-top {
    position: absolute; top: 9px; height: 32px;
    background: var(--tile-light); color: var(--navy);
    display: flex; align-items: center; justify-content: center;
    font-weight: 700; font-size: 17px; text-transform: uppercase;
  }

  .tagline-band {
    position: absolute; left: 0; top: 743px; width: 857px; height: 143px;
    background: var(--green); color: var(--white); text-align: center;
    text-transform: uppercase; font-weight: 400;
  }
  .tagline-band .line1 { position: absolute; top: 20px; width: 100%; font-size: 45px; }
  .tagline-band .line2 { position: absolute; top: 72px; width: 100%; font-size: 37px; }
  .tagline-band .line2 .today { font-size: 57px; line-height: 1; }

  .details { position: absolute; left: 0; top: 903px; width: 857px; text-align: center; }
  .details .intro { font-size: 19.5px; line-height: 1.35; padding: 0 55px; }
  .details .dates { font-size: 25px; font-weight: 700; text-transform: uppercase; margin-top: 10px; }
  .details .dates span { text-transform: none; }
  .details .closing { font-size: 19.5px; line-height: 1.35; margin-top: 6px; padding: 0 80px; }

  .rule { position: absolute; left: 0; top: 1076px; width: 857px; height: 3px; background: var(--green); }

  .host { position: absolute; top: 1092px; height: 92px; display: flex; align-items: center; gap: 8px; font-weight: 700; font-size: 16px; line-height: 1.1; }
  .host-left { left: 50px; width: 190px; color: var(--forest); }
  .host-right { left: 640px; width: 190px; color: var(--blue); justify-content: flex-end; text-align: right; }
  .host-mark { flex: none; }

  .register { position: absolute; left: 240px; top: 1104px; width: 377px; text-align: center; font-size: 21px; line-height: 1.45; }
</style>
</head>
<body>
<main class="flyer">
  <div class="hero-photo" role="img" aria-label="Photo of a group of hikers walking single file along a forest trail through tall grass and pine trees, with a dog at the back"></div>

  <div class="event-mark">
    <svg class="host-mark" width="26" height="26" viewBox="0 0 26 26" aria-hidden="true"><circle cx="13" cy="13" r="12" fill="var(--sun)"/></svg>
    <span>Campfest</span>
  </div>

  <h1 class="headline">
    <span class="strong">Don’t miss this</span>
    <span class="light">LGBT camping</span>
    <span class="strong">event!</span>
  </h1>

  <section class="sponsor-band" aria-label="Sponsors">
    <p class="sponsor-label">Sponsored by</p>
    <div class="sponsor-top" style="left:445px;width:189px;">Bluestem Outfitters</div>
    <div class="sponsor-top" style="left:642px;width:189px;">Harlan Brooks</div>
    <div class="sponsor-tile tile-grey" style="left:27px;width:132px;">Ridgeline Physio</div>
    <div class="sponsor-tile tile-light" style="left:163px;width:140px;">Maple Hall</div>
    <div class="sponsor-tile tile-light" style="left:309px;width:139px;">Open Summit</div>
    <div class="sponsor-tile tile-light" style="left:453px;width:132px;">trailnote.org</div>
    <div class="sponsor-tile tile-dark" style="left:590px;width:103px;">Vista FM</div>
    <div class="sponsor-tile tile-dark" style="left:698px;width:133px;">Juniper Mart</div>
  </section>

  <section class="tagline-band">
    <p class="line1">Plan the highlight of your</p>
    <p class="line2">Summer <span class="today">Today.</span></p>
  </section>

  <section class="details">
    <p class="intro">It’s almost time for the Rocky Mountain Region’s largest LGBT pride camping event: Campfest!</p>
    <p class="dates">Join us <span>August 8th -12th for 5 days</span></p>
    <p class="closing">of fun in a friendly, safe, LGBT affirming environment for everyone, from everywhere!</p>
  </section>

  <div class="rule"></div>

  <div class="host host-left">
    <svg class="host-mark" width="40" height="40" viewBox="0 0 40 40" aria-hidden="true"><circle cx="20" cy="20" r="18" fill="var(--forest)"/></svg>
    <span>Pinecrest Trail Council</span>
  </div>

  <p class="register">More information or register online<br>www.sagebrightfest.org</p>

  <div class="host host-right">
    <span>Prairie Alliance</span>
    <svg class="host-mark" width="36" height="36" viewBox="0 0 36 36" aria-hidden="true"><rect width="36" height="36" fill="var(--blue)"/></svg>
  </div>
</main>
</body>
</html>
```